Tollard Cove Marina Website

Business Background
Tollard Cove Marine is a full-service marina situated in Tollard Sound just two miles west of Tollard Inlet. Our 2 1/2 acres of waterfront real estate includes over 50 wet slips, jetski ports and dry storage that can accommodate boats as small as 13′ to boats up to 50′ in length. Our boaters are offered a safe, secure and family friendly environment while our staff is able to provide almost any service you could need for your boat to include shrink wrapping, bottom painting, detailing, mechanical repairs, new/used boat sales and much much more.

Would like a tab for the following:

Marina (summer dockage & winter storage)
Under marina tab list the following
FEATURES
All of our floating docks offer dockside electric, and water.
Summer Dockage
Need a place to keep your boat?
Winter & Summer Storage
Need a place to stay? We offer full transient dockage.
Transient Dockage
With easy access from the Pellow Creek
On site mechanical services provided.
Mechanical Services
Don't worry if you're forgetting something. We offer a full range of boating necessities.
Bait, Ice & Ship Store
Both long, and short haul services are available.
35 ton Open-End Travel Lift & Forklift
Our marina offers an keyfob access electronic gate, as well as video surveillance.
Security
Member only restroom, and shower.
Full Bathroom Facilities
Just minutes from Great Gun & Tollard Inlet
Ideal Fishermen Location
On site charters

Harborline Assist
Outboard Repairs & Repowers (using ferrow & kesta)
New Boat sales
Used Boat sales
Contact us

Link on home page to Facebook and Instagram
live weather link and noaa link

Industry/Entity Type

Marina

Coding

Coded - Design and coding required

Number of Pages Required

1 page

Colors
0054AA
0677BA
7BADD7
CADEEF
E8F1F8

Requirements
Must have
• Multiple pages prefer a dark page with blue like my logo

```html
<!DOCTYPE html>
<html lang="en">
<head>
<meta charset="utf-8">
<title>Tollard Cove Marine</title>
<link href="https://fonts.googleapis.com/css2?family=Montserrat:wght@400;500;600;700&family=Roboto+Condensed:wght@700&display=swap" rel="stylesheet">
<style>
:root{
  --accent:#2bbded;
  --ink:#1d1d1d;
  --white:#ffffff;
  --field:#dcdcdc;
  --footer:#2bbded;
}
*{box-sizing:border-box;margin:0;padding:0}
html,body{width:1200px;height:3475px;overflow:hidden}
body{font-family:'Montserrat',sans-serif;color:var(--ink);background:var(--white);position:relative}
.abs{position:absolute}
.heading{font-family:'Roboto Condensed',sans-serif;font-weight:700;color:var(--accent);text-transform:uppercase;letter-spacing:1px}
.btn{display:flex;align-items:center;justify-content:center;background:var(--accent);color:var(--white);font-weight:700;text-transform:uppercase;font-size:18px;border-radius:2px}

/* header */
.site-header{position:absolute;top:0;left:0;width:1200px;height:93px;background:var(--white);border-bottom:1px solid #e5e5e5}
.brand{left:81px;top:32px;display:flex;align-items:center;gap:10px;font-weight:700;font-size:17px;color:#1d1d1d;text-transform:uppercase;white-space:nowrap}
.brand .dot{width:22px;height:22px;border-radius:50%;background:var(--accent)}
.phone{right:245px;top:5px;display:flex;align-items:center;gap:6px;font-family:'Roboto Condensed',sans-serif;font-weight:700;font-size:23px;letter-spacing:.5px;white-space:nowrap}
.social{right:81px;top:4px;display:flex;gap:6px}
.social span{width:30px;height:30px;border-radius:8px;display:block}
.nav{right:81px;top:56px;display:flex;align-items:center;gap:37px;font-size:13px;font-weight:500;text-transform:uppercase;white-space:nowrap}
.nav .nav-cta{background:var(--accent);color:var(--white);padding:7px 13px;margin-left:-20px}

/* hero */
.hero{top:93px;left:0;width:1200px;height:572px;background:linear-gradient(180deg,#4a5b55 0%,#2f3f3f 40%,#1f2d33 75%,#2a3a3c 100%)}
.hero h1{position:absolute;top:158px;width:100%;text-align:center;color:var(--white);font-size:65px;font-weight:600;line-height:70px;text-transform:uppercase;letter-spacing:1px}
.hero .btn{position:absolute;left:503px;top:314px;width:194px;height:49px}

/* welcome */
.welcome{top:665px;left:0;width:1200px;height:508px}
.welcome h2{position:absolute;left:81px;top:70px;font-size:37px;white-space:nowrap}
.welcome .copy{position:absolute;left:81px;top:118px;width:430px;font-size:17.5px;line-height:24.2px}
.welcome .copy p+p{margin-top:24px}
.photo-main{position:absolute;left:615px;top:79px;width:465px;height:291px;border-radius:6px;background:linear-gradient(135deg,#3a6a86,#264f68 55%,#9fb4c1)}
.photo-small{position:absolute;left:954px;top:236px;width:167px;height:182px;border-radius:6px;border:5px solid var(--white);background:linear-gradient(180deg,#6ea4cf,#a9b9c2 60%,#7d8585)}

/* features */
.features{top:1173px;left:0;width:1200px;height:579px;background:linear-gradient(180deg,#15253a 0%,#1d3347 50%,#2a3e4e 80%,#5a4a3a 100%)}
.features h2,.services h2,.reviews h2{position:absolute;width:100%;text-align:center;font-size:78px;line-height:80px}
.features h2{top:68px}
.feature-list{position:absolute;top:190px;list-style:none;color:var(--white);font-size:20.5px;font-weight:500}
.feature-list li{display:flex;align-items:center;gap:10px;height:48px;white-space:nowrap}
.feature-list.left{left:156px}
.feature-list.right{left:704px}
.features .btn{position:absolute;left:503px;top:450px;width:194px;height:49px}

/* services */
.services{top:1752px;left:0;width:1200px;height:580px}
.services h2{top:68px}
.service-card{position:absolute;top:178px;width:247px;height:321px;border-radius:4px;overflow:hidden}
.service-card .cap{position:absolute;left:0;bottom:0;width:100%;height:58px;background:rgba(20,30,40,.7);color:var(--white);font-size:18.5px;text-transform:uppercase;display:flex;align-items:center;justify-content:center;text-align:center;line-height:19px}

/* reviews */
.reviews{top:2332px;left:0;width:1200px;height:429px;background:linear-gradient(180deg,#2d2b33 0%,#3d3538 30%,#2a3544 65%,#1f2a38 100%)}
.reviews h2{top:75px}
.stars{position:absolute;top:180px;width:100%;text-align:center;color:#f5c518;font-size:22px;letter-spacing:2px}
.quote{position:absolute;top:210px;width:100%;text-align:center;color:var(--white);font-size:20px;line-height:24px}
.reviewer{position:absolute;top:270px;width:100%;text-align:center;color:var(--accent);font-size:27px}
.dots{position:absolute;top:335px;width:100%;display:flex;justify-content:center;gap:10px}
.dots span{width:11px;height:11px;border-radius:50%;background:var(--white)}
.dots span.active{background:#f5c518}

/* contact */
.contact{top:2761px;left:0;width:1200px;height:465px}
.contact h2{position:absolute;left:79px;top:72px;font-size:78px;line-height:80px}
.contact-line{position:absolute;left:81px;display:flex;gap:12px;font-size:17.5px;line-height:24px}
.field{position:absolute;left:615px;width:504px;background:var(--field);color:#555;font-size:16px;padding:10px 18px}
.contact .btn{position:absolute;left:616px;top:376px;width:193px;height:47px}

/* footer */
.site-footer{top:3226px;left:0;width:1200px;height:194px;background:var(--footer)}
.footer-brand{left:81px;top:72px;display:flex;align-items:center;gap:10px;color:var(--white);font-weight:700;font-size:17px;text-transform:uppercase;white-space:nowrap}
.footer-brand .dot{width:22px;height:22px;border-radius:50%;background:var(--white)}
.footer-links{left:511px;top:36px;list-style:none;color:var(--white);font-size:12.5px;font-weight:700;text-transform:uppercase}
.footer-links li{height:34px}
.footer-social{right:81px;top:34px;display:flex;gap:8px}
.footer-social span{width:56px;height:56px;border-radius:8px;display:block;border:4px solid var(--white)}
.copyright{top:3420px;left:0;width:1200px;height:55px;display:flex;align-items:center;justify-content:center;font-size:12.5px;font-weight:500;text-transform:uppercase}
</style>
</head>
<body>

<header class="site-header">
  <div class="abs brand"><span class="dot"></span>Tollard Cove Marine</div>
  <div class="abs phone">
    <svg width="24" height="24" viewBox="0 0 24 24"><path d="M6.6 10.8a15 15 0 0 0 6.6 6.6l2.2-2.2a1 1 0 0 1 1-.25 11 11 0 0 0 3.6.6 1 1 0 0 1 1 1V20a1 1 0 0 1-1 1A17 17 0 0 1 3 4a1 1 0 0 1 1-1h3.5a1 1 0 0 1 1 1 11 11 0 0 0 .6 3.6 1 1 0 0 1-.25 1z" fill="#2bbded"/></svg>
    555-014-2290
  </div>
  <div class="abs social">
    <span style="background:#d63a7a"></span>
    <span style="background:#2a6bd6"></span>
    <span style="background:#8fd0f0"></span>
    <span style="background:#1d4f9a;border-radius:50%"></span>
  </div>
  <nav class="abs nav">
    <span>Home</span><span>Features</span><span>Harborline Assist</span><span>New Boat Sales</span><span>Used Boat Sales</span><span class="nav-cta">Contact Us</span>
  </nav>
</header>

<section class="abs hero" role="img" aria-label="Aerial view of the marina docks and moored boats">
  <h1>Lorem ipsum dolor sit<br>amet consectetur</h1>
  <div class="btn">Contact Us</div>
</section>

<section class="abs welcome">
  <h2 class="heading">Welcome to Tollard Cove</h2>
  <div class="copy">
    <p>Tollard Cove Marine is a full-service marina situated in Tollard Sound just two miles west of Tollard Inlet. Our 2 1/2 acres of waterfront real estate includes over 50 wet slips, jetski ports and dry storage that can accommodate boats as small as 13' to boats up to 50' in length.</p>
    <p>Our boaters are offered a safe, secure and family friendly environment while our staff is able to provide almost any service you could need for your boat to include shrink wrapping, bottom painting, detailing, mechanical repairs, new/used boat sales and much much more.</p>
  </div>
  <div class="photo-main" role="img" aria-label="Motor yacht cruising across open water"></div>
  <div class="photo-small" role="img" aria-label="Boat lifted in the travel lift"></div>
</section>

<section class="abs features" role="img" aria-label="View from a boat bow over the harbour at dusk">
  <h2 class="heading">Features</h2>
  <ul class="feature-list left">
    <li><svg width="22" height="22" viewBox="0 0 22 22"><rect x="2" y="3" width="16" height="16" rx="3" fill="none" stroke="#2bbded" stroke-width="2"/><path d="M6 10l4 4 10-11" fill="none" stroke="#2bbded" stroke-width="2.4"/></svg>Summer Dockage</li>
    <li><svg width="22" height="22" viewBox="0 0 22 22"><rect x="2" y="3" width="16" height="16" rx="3" fill="none" stroke="#2bbded" stroke-width="2"/><path d="M6 10l4 4 10-11" fill="none" stroke="#2bbded" stroke-width="2.4"/></svg>Winter &amp; Summer Storage</li>
    <li><svg width="22" height="22" viewBox="0 0 22 22"><rect x="2" y="3" width="16" height="16" rx="3" fill="none" stroke="#2bbded" stroke-width="2"/><path d="M6 10l4 4 10-11" fill="none" stroke="#2bbded" stroke-width="2.4"/></svg>Transient Dockage</li>
    <li><svg width="22" height="22" viewBox="0 0 22 22"><rect x="2" y="3" width="16" height="16" rx="3" fill="none" stroke="#2bbded" stroke-width="2"/><path d="M6 10l4 4 10-11" fill="none" stroke="#2bbded" stroke-width="2.4"/></svg>Mechanical Services</li>
    <li><svg width="22" height="22" viewBox="0 0 22 22"><rect x="2" y="3" width="16" height="16" rx="3" fill="none" stroke="#2bbded" stroke-width="2"/><path d="M6 10l4 4 10-11" fill="none" stroke="#2bbded" stroke-width="2.4"/></svg>Bait, Ice &amp; Ship Store</li>
  </ul>
  <ul class="feature-list right">
    <li><svg width="22" height="22" viewBox="0 0 22 22"><rect x="2" y="3" width="16" height="16" rx="3" fill="none" stroke="#2bbded" stroke-width="2"/><path d="M6 10l4 4 10-11" fill="none" stroke="#2bbded" stroke-width="2.4"/></svg>Security</li>
    <li><svg width="22" height="22" viewBox="0 0 22 22"><rect x="2" y="3" width="16" height="16" rx="3" fill="none" stroke="#2bbded" stroke-width="2"/><path d="M6 10l4 4 10-11" fill="none" stroke="#2bbded" stroke-width="2.4"/></svg>Full Bathroom Facilities</li>
    <li><svg width="22" height="22" viewBox="0 0 22 22"><rect x="2" y="3" width="16" height="16" rx="3" fill="none" stroke="#2bbded" stroke-width="2"/><path d="M6 10l4 4 10-11" fill="none" stroke="#2bbded" stroke-width="2.4"/></svg>Ideal Fishermen Location</li>
    <li><svg width="22" height="22" viewBox="0 0 22 22"><rect x="2" y="3" width="16" height="16" rx="3" fill="none" stroke="#2bbded" stroke-width="2"/><path d="M6 10l4 4 10-11" fill="none" stroke="#2bbded" stroke-width="2.4"/></svg>On site charters</li>
  </ul>
  <div class="btn">Learn More</div>
</section>

<section class="abs services">
  <h2 class="heading">Our Services</h2>
  <div class="service-card" style="left:81px;background:linear-gradient(180deg,#b9d3ea 0%,#dfe6ec 45%,#c8262b 70%,#3a3a3a 100%)" role="img" aria-label="Assist towboat at the dock">
    <div class="cap">Harborline Assist</div>
  </div>
  <div class="service-card" style="left:345px;background:linear-gradient(180deg,#5f8fc4 0%,#a8bccb 50%,#6b6f70 100%)" role="img" aria-label="Boat held in the travel lift for repairs">
    <div class="cap">Outboard<br>Repairs &amp; Repowers</div>
  </div>
  <div class="service-card" style="left:609px;background:linear-gradient(180deg,#9fc0dc 0%,#7b8c6e 35%,#e9eef2 60%,#1c2a4a 100%)" role="img" aria-label="New motor yacht at anchor">
    <div class="cap">New Boat Sales</div>
  </div>
  <div class="service-card" style="left:871px;background:linear-gradient(180deg,#d6e0e8 0%,#b6c6d1 45%,#f2f4f5 65%,#2a7fa6 100%)" role="img" aria-label="Used sport cruiser under way">
    <div class="cap">Used Boat Sales</div>
  </div>
</section>

<section class="abs reviews" role="img" aria-label="Motor yacht on the water at sunset">
  <h2 class="heading">What People Talk</h2>
  <div class="stars">★★★★★</div>
  <p class="quote">Lorem ipsum dolor sit amet, consectetur adipiscing elit, sed do<br>eiusmod tempor incididunt ut labore et dolore magna aliqua.</p>
  <div class="reviewer">Dana K</div>
  <div class="dots"><span class="active"></span><span></span><span></span></div>
</section>

<section class="abs contact">
  <h2 class="heading">Contact</h2>
  <div class="contact-line" style="top:177px">
    <svg width="20" height="24" viewBox="0 0 20 24"><path d="M10 1a8 8 0 0 0-8 8c0 6 8 14 8 14s8-8 8-14a8 8 0 0 0-8-8z" fill="#2bbded"/><circle cx="10" cy="9" r="3" fill="#fff"/></svg>
    <span>48 Wharfside Lane, Tollard Cove,<br>New York 10099, &nbsp;United States</span>
  </div>
  <div class="contact-line" style="top:251px">
    <svg width="20" height="20" viewBox="0 0 24 24"><path d="M6.6 10.8a15 15 0 0 0 6.6 6.6l2.2-2.2a1 1 0 0 1 1-.25 11 11 0 0 0 3.6.6 1 1 0 0 1 1 1V20a1 1 0 0 1-1 1A17 17 0 0 1 3 4a1 1 0 0 1 1-1h3.5a1 1 0 0 1 1 1 11 11 0 0 0 .6 3.6 1 1 0 0 1-.25 1z" fill="#2bbded"/></svg>
    <span>555-014-2290</span>
  </div>
  <div class="contact-line" style="top:286px">
    <svg width="20" height="20" viewBox="0 0 20 20"><rect x="1" y="4" width="18" height="12" fill="#2bbded"/><path d="M1 4l9 7 9-7" fill="none" stroke="#fff" stroke-width="1.5"/></svg>
    <span>dockmaster@tollardcovemarine.com</span>
  </div>
  <div class="field" style="top:81px;height:46px">Name</div>
  <div class="field" style="top:136px;height:44px">Tel no.</div>
  <div class="field" style="top:191px;height:45px">Email</div>
  <div class="field" style="top:245px;height:108px">Message</div>
  <div class="btn">Send</div>
</section>

<footer class="abs site-footer">
  <div class="abs footer-brand"><span class="dot"></span>Tollard Cove Marine</div>
  <ul class="abs footer-links">
    <li>Features</li><li>Harborline Assist</li><li>New Boat Sales</li><li>Used Boat Sales</li>
  </ul>
  <div class="abs footer-social">
    <span style="background:#d63a7a"></span>
    <span style="background:#2a6bd6"></span>
    <span style="background:#8fd0f0"></span>
    <span style="background:#1d4f9a"></span>
  </div>
</footer>
<div class="abs copyright">Copyright © 2024 Tollard Cove Marine - All Rights Reserved.</div>

</body>
</html>
```